Book Cover for a technology book - The Quiet Lattice

We are writing a book that is a handbook how to build a hybrid cloud - this is a technology concept where companies use cloud services both from the like of Vantrel or Orbisoft and also cloud services built in there own data centers - hence the term hybrid cloud. We want a book cover with the title - The Quiet Lattice; which signifies that we will be teaching companies how to build a hybrid cloud that just works. We want the tagline - handbook for building Hybrid Clouds. The authors are Warren Pelham and Tom Garvey. The cover is to be engaging and feel different than your usual technical manual. I don't have any graphics to help out however will be able to refine and tell you what I don and don't like based on your drafts. The book dimensions are yet to be determined, in the first instance it will be a PDF

Target Market(s)

technology executives and specialists

Industry/Entity Type

Information Technology

Colors

Designer to choose colors to be used in the design.

Requirements
Nice to have
• While I don't have a particular view to how it will look, I'd like the style to be more casual than ultra formal

```html
<!DOCTYPE html>
<html lang="en">
<head>
<meta charset="utf-8">
<title>The Quiet Lattice – Cover Spread</title>
<link rel="stylesheet" href="https://fonts.googleapis.com/css2?family=Exo+2:wght@300;800&family=Archivo+Black&display=swap">
<style>
  :root {
    --paper: #e5e8ee;
    --ink: #1c1c1c;
    --ribbon: #3358a8;
    --ribbon-deep: #25479a;
    --globe-light: #3d66c4;
    --globe-dark: #2a4aa0;
    --white: #ffffff;
  }
  html, body {
    margin: 0;
    padding: 0;
    width: 1200px;
    height: 733px;
    overflow: hidden;
    background: var(--white);
  }
  .spread { display: block; width: 1200px; height: 733px; }
  .paper { fill: var(--paper); }
  .band-dark { fill: var(--ink); }
  .ribbon { fill: var(--ribbon); }
  .ribbon-fold { fill: var(--ribbon-deep); }
  .gutter { fill: var(--white); }
  .globe-frame { fill: var(--white); }
  .title {
    font-family: "Exo 2", sans-serif;
    font-weight: 800;
    fill: var(--white);
    font-size: 44px;
  }
  .tagline {
    font-family: "Exo 2", sans-serif;
    font-weight: 300;
    fill: var(--white);
    font-size: 17px;
  }
  .authors {
    font-family: "Archivo Black", sans-serif;
    fill: var(--white);
    font-size: 23px;
  }
  .spine-title {
    font-family: "Exo 2", sans-serif;
    font-weight: 800;
    fill: var(--white);
    font-size: 32px;
  }
  .spine-tagline {
    font-family: "Exo 2", sans-serif;
    font-weight: 300;
    fill: var(--ink);
    font-size: 17px;
  }
  .spine-authors {
    font-family: "Archivo Black", sans-serif;
    fill: var(--ink);
    font-size: 23px;
  }
</style>
</head>
<body>
<svg class="spread" viewBox="0 0 1500 916" xmlns="http://www.w3.org/2000/svg">
  <defs>
    <radialGradient id="globe-fill" cx="45%" cy="40%" r="65%">
      <stop offset="0" stop-color="#4b74cf"/>
      <stop offset="1" stop-color="#2a4aa0"/>
    </radialGradient>
  </defs>

  <!-- back cover -->
  <g class="back-cover">
    <rect class="paper" x="0" y="0" width="695" height="916"/>
    <polygon class="ribbon" points="350,133 383,133 300,275 222,275"/>
    <polygon class="ribbon-fold" points="383,133 400,181 370,181"/>
    <polygon class="band-dark" points="330,181 695,181 695,465 200,465"/>
    <rect class="ribbon" x="430" y="465" width="265" height="87"/>
    <polygon class="band-dark" points="0,465 432,465 215,916 0,916"/>
    <circle class="globe-frame" cx="265" cy="463" r="203"/>
    <circle cx="265" cy="463" r="178" fill="url(#globe-fill)" role="img"
            aria-label="Network globe of connected nodes with cloud, device and service icons"/>
    <text class="title" x="400" y="233">The Quiet</text>
    <text class="title" x="400" y="272">Lattice</text>
    <text class="tagline" x="399" y="294">Handbook For Building Hybrid Clouds</text>
    <text class="authors" x="22" y="868">Warren Pelham</text>
    <text class="authors" x="22" y="893">Tom Garvey.</text>
  </g>

  <rect class="gutter" x="695" y="0" width="5" height="916"/>

  <!-- spine -->
  <g class="spine">
    <rect class="paper" x="700" y="0" width="97" height="916"/>
    <rect class="band-dark" x="700" y="0" width="97" height="22"/>
    <rect class="band-dark" x="700" y="28" width="97" height="437"/>
    <rect class="ribbon" x="700" y="465" width="97" height="87"/>
    <text class="spine-title" transform="translate(748,82) rotate(90)">The Quiet Lattice</text>
    <text class="spine-tagline" transform="translate(728,82) rotate(90)">Handbook For Building Hybrid Clouds</text>
    <text class="spine-authors" transform="translate(752,712) rotate(90)">Warren Pelham</text>
    <text class="spine-authors" transform="translate(727,712) rotate(90)">Tom Garvey.</text>
  </g>

  <rect class="gutter" x="797" y="0" width="9" height="916"/>

  <!-- front cover -->
  <g class="front-cover">
    <rect class="paper" x="806" y="0" width="694" height="916"/>
    <polygon class="ribbon" points="808,0 862,0 1392,916 1338,916"/>
    <polygon class="band-dark" points="806,303 1115,303 1238,488 1135,488 1500,488 1500,648 1240,648 1135,488 806,488"/>
    <polygon class="ribbon-fold" points="806,488 870,488 806,585"/>
    <polygon class="ribbon" points="1380,648 1500,648 1420,752 1310,752"/>
    <text class="title" x="840" y="380">The Quiet</text>
    <text class="title" x="840" y="418">Lattice</text>
    <text class="tagline" x="839" y="440">Handbook For Building Hybrid Clouds</text>
  </g>
</svg>
</body>
</html>
```